Business Card - Rebranding for Consulting Firm

We are renaming and rebranding our consulting firm and need to raise the level of quality of our cards as part of that effort. We consult to leading high tech, life science and other innovation sector companies.

Need a two-sided business card design.

Side 1: (a) Company logo (b) tag line: Get More From the People You Hire (c) Name (d) Title (e) Phone 1: Office (f) Phone 2: Mobile (g) email: person@HollowmereAdvisory.com

Side 2: Two lines of text: (a) Markets Keep Moving. Plans Need Focus. People Turn Plans Into Results. (b) We help you excel at all three.

Target Market(s)

Business and human resources executives and senior managers

Industry/Entity Type

Management Consulting

Contact Information for Business Card

Font styles to use
Sans Serif

Requirements
Must have
• clean, not too busy, but with a bit of creativity. Stick to the colors used in the attached logo
• appeal to high tech, life science companies
Nice to have
• prefer white background

```html
<!DOCTYPE html>
<html lang="en">
<head>
<meta charset="utf-8">
<title>Hollowmere Advisory — Business Card</title>
<link rel="stylesheet" href="https://fonts.googleapis.com/css2?family=Open+Sans:wght@400;600;700&family=Crimson+Text:ital@1&display=swap">
<style>
  :root {
    --page: #e4e7eb;
    --card: #eef3f9;
    --navy: #1f3d6b;
    --blue: #1a86c7;
    --sky: #2aa9e0;
    --ink: #5a5f66;
    --white: #ffffff;
  }
  * { margin: 0; padding: 0; box-sizing: border-box; }
  html, body { width: 1200px; height: 876px; overflow: hidden; }
  body {
    background: var(--page);
    font-family: "Open Sans", Arial, sans-serif;
    position: relative;
  }
  .card {
    position: absolute;
    left: 240px;
    width: 720px;
    height: 400px;
    background: var(--card);
    overflow: hidden;
    box-shadow: 0 6px 18px rgba(0,0,0,0.18);
  }
  .card--back { top: 26px; }
  .card--front { top: 450px; }
  .card__shapes { position: absolute; inset: 0; width: 720px; height: 400px; }

  .brand { display: flex; align-items: center; gap: 10px; }
  .brand__mark { width: 22px; height: 22px; background: var(--blue); flex: none; }
  .brand__name {
    font-weight: 600;
    color: var(--navy);
    font-size: 30px;
    letter-spacing: -0.3px;
    line-height: 1;
    white-space: nowrap;
  }
  .tagline {
    font-family: "Crimson Text", Georgia, serif;
    font-style: italic;
    color: var(--sky);
    white-space: nowrap;
  }

  /* Back side */
  .back__content {
    position: absolute;
    left: 0; right: 0; top: 108px;
    display: flex; flex-direction: column; align-items: center;
  }
  .back__content .tagline { font-size: 22px; line-height: 1.35; text-align: center; }
  .back__content .brand { margin-bottom: 36px; }

  /* Front side */
  .front__brand { position: absolute; left: 40px; top: 72px; }
  .front__brand .brand__name { font-size: 27px; }
  .front__brand .brand__mark { width: 20px; height: 20px; }
  .front__brand .tagline { font-size: 21px; margin-top: 8px; }
  .person { position: absolute; right: 92px; top: 92px; text-align: right; }
  .person__name { font-weight: 700; font-size: 19px; color: var(--navy); letter-spacing: 0.3px; }
  .person__title { font-size: 14px; color: var(--blue); letter-spacing: 3px; margin-top: 6px; }
  .online { position: absolute; right: 92px; top: 198px; text-align: right; color: var(--ink); font-size: 15px; line-height: 1.45; }
  .online__icons { position: absolute; right: 18px; top: 196px; display: flex; flex-direction: column; gap: 10px; }
  .phones { position: absolute; left: 40px; top: 240px; list-style: none; }
  .phones li { display: flex; align-items: center; gap: 14px; color: var(--ink); font-size: 15px; letter-spacing: 1px; height: 25px; }
  .phones svg { width: 14px; height: 16px; fill: var(--blue); }
  .address {
    position: absolute; left: 282px; top: 326px;
    display: flex; align-items: center; gap: 8px;
    color: var(--white); font-size: 15px;
    white-space: nowrap;
  }
  .address svg { width: 14px; height: 18px; fill: var(--white); }
</style>
</head>
<body>

<section class="card card--back" aria-label="Card back">
  <svg class="card__shapes" viewBox="0 0 720 400" aria-hidden="true">
    <polygon points="0,372 720,306 720,328 0,394" fill="var(--white)"/>
    <polygon points="0,388 720,322 720,400 0,400" fill="var(--blue)"/>
  </svg>
  <div class="back__content">
    <div class="brand">
      <span class="brand__mark"></span>
      <span class="brand__name">Hollowmere Advisory LLC</span>
    </div>
    <p class="tagline">Markets Keep Moving. Plans Need Focus. People Turn Plans Into Results.</p>
    <p class="tagline">Get More From the People You Hire</p>
  </div>
</section>

<section class="card card--front" aria-label="Card front">
  <svg class="card__shapes" viewBox="0 0 720 400" aria-hidden="true">
    <polygon points="520,0 720,0 720,44 560,44" fill="var(--sky)"/>
    <rect x="662" y="0" width="58" height="300" fill="var(--sky)"/>
    <polygon points="0,372 720,330 720,400 0,400" fill="var(--blue)"/>
    <polygon points="232,361 262,312 720,300 720,330" fill="var(--sky)"/>
  </svg>

  <div class="front__brand">
    <div class="brand">
      <span class="brand__mark"></span>
      <span class="brand__name">Hollowmere Advisory LLC</span>
    </div>
    <p class="tagline">Get More From the People You Hire</p>
  </div>

  <div class="person">
    <p class="person__name">PERSONS NAME</p>
    <p class="person__title">PERSONS TITLE</p>
  </div>

  <div class="online">
    <p>aaaaaa@nnn.com</p>
    <p>www.sssssss.com</p>
  </div>
  <div class="online__icons" aria-hidden="true">
    <svg width="14" height="10" viewBox="0 0 14 10"><rect width="14" height="10" fill="var(--white)"/><polyline points="0,0 7,6 14,0" fill="none" stroke="var(--sky)" stroke-width="1.5"/></svg>
    <svg width="14" height="14" viewBox="0 0 14 14"><circle cx="7" cy="7" r="6" fill="none" stroke="var(--white)" stroke-width="1.6"/><ellipse cx="7" cy="7" rx="2.5" ry="6" fill="none" stroke="var(--white)" stroke-width="1.2"/></svg>
  </div>

  <ul class="phones">
    <li><svg viewBox="0 0 14 16" aria-hidden="true"><path d="M3 1 L6 1 L7 5 L5 6.5 Q6.5 10 9 11 L10.5 9 L13 10.5 L13 14 Q6 15 1.5 7 Q1 3 3 1Z"/></svg>(999) 222-5555</li>
    <li><svg viewBox="0 0 14 16" aria-hidden="true"><path d="M3 0 H11 V16 H3Z M4.5 2 V12 H9.5 V2Z"/></svg>(999) 222-4444</li>
    <li><svg viewBox="0 0 14 16" aria-hidden="true"><path d="M3 1 H11 V5 H3Z M0 6 H14 V12 H12 V10 H2 V12 H0Z M3 11 H11 V15 H3Z"/></svg>(999) 222-3333</li>
  </ul>

  <p class="address">
    <svg viewBox="0 0 14 18" aria-hidden="true"><path d="M7 0 A7 7 0 0 1 14 7 C14 12 7 18 7 18 C7 18 0 12 0 7 A7 7 0 0 1 7 0Z M7 4 A3 3 0 1 0 7 10 A3 3 0 1 0 7 4Z"/></svg>
    City, State Name, 77 Street Name str.
  </p>
</section>

</body>
</html>
```